Harbourline Advisory Group Wordpress Design

See attached brief. If you have questions beyond this please let me know. Brief document is HA Group Website Design v1. Other documents are files from logo creation and business cards to give you an idea of colours and images. Also see document that shows examples of the types of images I want to display on the website.

Focus of site is for customers and to drive traffic from social media etc. Company is startup consulting business in Customer Experience and Contact Centre. We offer benchmarking, strategy reviews, technology audits. etc

Looking for the site to use the existing Wordpress theme on Nestora or something compatible. Happy to change if there is a good reason for doing so.

Has to be easy to manage ongoing if possible.

Target Market(s)

HAG is a consulting organisation in contact centre and customer experience

Number of Pages Required

4 page

Font styles to use
Serif
Sans Serif

Colors
0255a3
3276b5
33a6d7
0293ce
ffffff
fefdec

Requirements
Must have
• Hosted on Nestora so must be compatible. Preference is to use the theme that is already there (Lumeo) unless there is a reason not to
Nice to have
• see brief

```html
<!DOCTYPE html>
<html lang="en">
<head>
<meta charset="utf-8">
<title>Harbourline Advisory Group</title>
<link href="https://fonts.googleapis.com/css2?family=Oswald:wght@300;400;500&family=PT+Sans:wght@400;700&family=Open+Sans:wght@400;600;700&display=swap" rel="stylesheet">
<style>
:root{
  --blue:#0aa4ea;
  --blue-deep:#0255a3;
  --blue-mid:#3276b5;
  --ink:#1d1d1d;
  --text:#555;
  --muted:#888;
  --dark:#3a4450;
  --white:#fff;
  --line:#d6d6d6;
}
*{margin:0;padding:0;box-sizing:border-box}
html,body{width:1200px;height:3303px;overflow:hidden}
body{position:relative;background:var(--white);font-family:"Open Sans",sans-serif;color:var(--text)}
.abs{position:absolute}
.wordmark{font-family:"PT Sans",sans-serif;font-weight:700;letter-spacing:.5px;display:flex;align-items:center;gap:10px}
.wordmark .mark{width:14px;height:14px;border-radius:50%;display:block}

/* hero */
.hero{left:0;top:0;width:1200px;height:876px;background:linear-gradient(135deg,#8b9199 0%,#c9ccd0 40%,#e3e4e6 60%,#9aa0a6 100%)}
.hero-nav{top:52px;left:99px;right:99px;display:flex;justify-content:space-between;align-items:center}
.hero-nav .wordmark{color:var(--blue-deep);font-size:15px}
.hero-nav .wordmark .mark{background:var(--blue-deep)}
.menu{display:flex;gap:24px;font-size:12px;color:var(--white);align-items:center}
.search{width:13px;height:13px}
.hero-title{left:99px;top:305px;color:var(--white);font-family:"Oswald",sans-serif;line-height:1}
.hero-title .l1{font-weight:300;font-size:78px}
.hero-title .l2{font-weight:500;font-size:80px;margin-top:2px}
.hero-title .l3{font-weight:300;font-size:46px;margin-top:4px}
.btn-ghost{left:99px;top:533px;width:140px;height:44px;border:2px solid var(--white);color:var(--white);font-family:"Oswald",sans-serif;font-size:14px;display:flex;align-items:center;justify-content:center}
.arrow{top:424px;width:50px;height:50px;display:flex;align-items:center;justify-content:center}
.arrow.prev{left:0;background:rgba(40,40,40,.7)}
.arrow.next{right:0;background:var(--blue)}
.thumb{left:1004px;top:376px;width:144px;height:137px;border:4px solid var(--blue);background:linear-gradient(135deg,#dfe5ea,#8fa4b4)}
.dots{display:flex;gap:8px}
.dots i{width:12px;height:12px;border-radius:50%;background:#ddd;display:block}
.dots i.on{background:var(--blue)}
.hero .dots{left:566px;top:835px}

/* sticky bar */
.bar{left:0;top:876px;width:1200px;height:62px;background:var(--blue);display:flex;justify-content:space-between;align-items:center;padding:0 99px}
.bar .wordmark{color:var(--white);font-size:16px}
.bar .wordmark .mark{background:var(--white)}

/* headings */
.section-title{left:0;width:1200px;text-align:center;font-family:"PT Sans",sans-serif;font-weight:700;color:var(--ink);font-size:36px}
.rule{left:568px;width:64px;height:6px;border-top:2px solid #bbb;border-bottom:2px solid #bbb}

/* welcome */
.lede{left:0;top:1086px;width:1200px;text-align:center;font-size:15px;color:var(--muted)}
.features{left:99px;top:1152px;width:1002px;display:flex;justify-content:space-between}
.feature{width:245px;text-align:center}
.feature .icon{width:88px;height:88px;border-radius:50%;background:#e9e9e9;border:2px solid #cfcfcf;margin:0 auto;display:flex;align-items:center;justify-content:center}
.feature .icon.on{background:var(--blue);border-color:var(--blue)}
.feature h3{font-size:15px;font-weight:700;color:var(--ink);margin-top:28px}
.feature p{font-size:12px;line-height:19px;margin-top:18px;color:#444}
.feature .more{display:block;font-family:"PT Sans",sans-serif;font-weight:700;font-size:14px;color:var(--ink);margin-top:26px}
.feature .more.on{color:var(--blue)}
.side-social{right:0;top:1072px;width:52px}
.side-social span{display:flex;align-items:center;justify-content:center;height:53px;background:var(--blue-mid)}
.side-social span+span{background:var(--blue)}
.side-social i{width:14px;height:14px;border-radius:50%;background:var(--white);display:block}

/* newsletter */
.newsletter{left:0;top:1469px;width:1200px;height:365px;background:linear-gradient(90deg,#2f3843,#48525d 55%,#3a434e)}
.newsletter h2{position:absolute;left:0;top:52px;width:1200px;text-align:center;color:var(--white);font-family:"PT Sans",sans-serif;font-weight:700;font-size:36px;line-height:48px}
.newsletter .rule{top:158px;border-color:#8a9099}
.newsletter .sub{position:absolute;left:0;top:172px;width:1200px;text-align:center;color:var(--blue);font-size:14px}
.field{border:2px solid #c9c9c9;height:46px}
.newsletter .field{position:absolute;top:251px;width:403px}
.submit{position:absolute;left:956px;top:251px;width:145px;height:46px;background:var(--blue);color:var(--white);font-family:"Oswald",sans-serif;font-size:14px;display:flex;align-items:center;justify-content:center}

/* blog */
.post{width:500px;height:187px;display:flex}
.post .photo{width:255px;height:187px}
.post .body{flex:1;padding:20px 30px 0}
.post.right{flex-direction:row-reverse}
.post.right .body{text-align:right}
.post h4{font-family:"Oswald",sans-serif;font-weight:400;color:var(--blue);font-size:19px;line-height:26px}
.post .meta{font-size:10px;color:#333;margin-top:6px;line-height:14px}
.post .meta b{color:var(--blue)}
.post .cont{display:inline-block;margin-top:10px;background:var(--blue);color:var(--white);font-family:"Oswald",sans-serif;font-size:11px;padding:0 10px;height:37px;line-height:37px;width:121px;text-align:center}

/* clients */
.clients{left:99px;top:2546px;width:1002px;height:128px;border-top:6px double #ccc;display:flex;justify-content:space-between;align-items:center;padding-top:10px}
.clients span{font-family:"PT Sans",sans-serif;font-weight:700;font-size:34px}

/* footer */
.footer{left:0;top:2697px;width:1200px;height:606px;background:linear-gradient(180deg,#3a72a6,#2f5f92 60%,#24527f)}
.footer .section-title{color:var(--white);top:50px;font-size:30px}
.footer .rule{top:106px;border-color:#9fbbd6}
.footer h5{position:absolute;color:var(--white);font-size:15px;font-weight:700}
.footer .copy{position:absolute;left:99px;top:181px;width:745px;color:#e3ecf5;font-size:12px;line-height:16px}
.footer .field{position:absolute;border:2px solid #c9d7e6;height:31px;color:#e6eef6;font-size:12px;padding:6px 14px}
.contact{position:absolute;left:870px;top:178px;color:var(--white);font-size:12px;line-height:15px}
.f-rule{position:absolute;height:5px;border-top:1px solid #a9c1d8;border-bottom:1px solid #a9c1d8}
.social-grid{position:absolute;left:870px;top:386px;width:230px;display:grid;grid-template-columns:repeat(8,18px);gap:14px 13px}
.social-grid i{width:14px;height:14px;border-radius:50%;background:var(--white);display:block}
.legal{position:absolute;left:99px;top:548px;color:#e6eef6;font-size:10px}
</style>
</head>
<body>

<header class="abs hero" role="img" aria-label="Photo of a business team meeting around a table, seen from above">
  <nav class="abs hero-nav">
    <div class="wordmark"><span class="mark"></span>HARBOURLINE ADVISORY GROUP</div>
    <div class="menu"><span>Home Page</span><span>Services</span><span>Partners</span><span>Blog</span><span>Get in Touch</span>
      <svg class="search" viewBox="0 0 14 14"><circle cx="6" cy="6" r="4.5" fill="none" stroke="#fff" stroke-width="2"/><line x1="9.5" y1="9.5" x2="13" y2="13" stroke="#fff" stroke-width="2"/></svg></div>
  </nav>
  <div class="abs hero-title"><div class="l1">HARBOURLINE</div><div class="l2">ADVISORY</div><div class="l3">GROUP</div></div>
  <div class="abs btn-ghost">READ MORE</div>
  <div class="abs arrow prev"><svg width="14" height="20" viewBox="0 0 14 20"><polyline points="10,3 3,10 10,17" fill="none" stroke="#fff" stroke-width="2"/></svg></div>
  <div class="abs arrow next"><svg width="14" height="20" viewBox="0 0 14 20"><polyline points="4,3 11,10 4,17" fill="none" stroke="#fff" stroke-width="2"/></svg></div>
  <div class="abs thumb" role="img" aria-label="Small photo of consultants at a desk"></div>
  <div class="abs dots"><i></i><i></i><i class="on"></i><i></i></div>
</header>

<div class="abs bar">
  <div class="wordmark"><span class="mark"></span>HARBOURLINE ADVISORY GROUP</div>
  <div class="menu"><span>Home Page</span><span>Services</span><span>Partners</span><span>Blog</span><span>Get in Touch</span>
    <svg class="search" viewBox="0 0 14 14"><circle cx="6" cy="6" r="4.5" fill="none" stroke="#fff" stroke-width="2"/><line x1="9.5" y1="9.5" x2="13" y2="13" stroke="#fff" stroke-width="2"/></svg></div>
</div>

<h1 class="abs section-title" style="top:986px">Welcome To Harbourline Advisory Group</h1>
<div class="abs rule" style="top:1046px"></div>
<p class="abs lede">This is the ultimate and definitive guide for an effective business plan for any type of startup.</p>

<div class="abs features">
  <div class="feature">
    <div class="icon"><svg width="36" height="36" viewBox="0 0 36 36"><path d="M8 28 L10 21 L24 7 L29 12 L15 26 Z" fill="none" stroke="#333" stroke-width="2"/><line x1="21" y1="10" x2="26" y2="15" stroke="#333" stroke-width="2"/></svg></div>
    <h3>Lorem Ipsum Dummy</h3>
    <p>Nulla consequat massa quis enim. Veronum versus Donec pede justo, fringilla vel, aliquet nec, vulputate eget, in enim justo, rhoncus ut, imperdiet a, venenatis vitae</p>
    <span class="more">Read More</span>
  </div>
  <div class="feature">
    <div class="icon on"><svg width="40" height="36" viewBox="0 0 40 36"><rect x="5" y="6" width="30" height="20" fill="none" stroke="#fff" stroke-width="2"/><line x1="14" y1="31" x2="26" y2="31" stroke="#fff" stroke-width="2"/><line x1="20" y1="26" x2="20" y2="31" stroke="#fff" stroke-width="2"/></svg></div>
    <h3>Lorem Ipsum Dummy</h3>
    <p>Nulla consequat massa quis enim. Veronum versus Donec pede justo, fringilla vel, aliquet nec, vulputate eget, in enim justo, rhoncus ut, imperdiet a, venenatis vitae</p>
    <span class="more on">Read More</span>
  </div>
  <div class="feature">
    <div class="icon"><svg width="36" height="36" viewBox="0 0 36 36"><rect x="11" y="4" width="14" height="28" rx="2" fill="none" stroke="#333" stroke-width="2"/><circle cx="18" cy="28" r="1.5" fill="#333"/></svg></div>
    <h3>Lorem Ipsum Dummy</h3>
    <p>Nulla consequat massa quis enim. Veronum versus Donec pede justo, fringilla vel, aliquet nec, vulputate eget, in enim justo, rhoncus ut, imperdiet a, venenatis vitae</p>
    <span class="more">Read More</span>
  </div>
  <div class="feature">
    <div class="icon"><svg width="40" height="36" viewBox="0 0 40 36"><path d="M4 18 Q20 4 36 18 Q20 32 4 18 Z" fill="#222"/><circle cx="20" cy="18" r="5" fill="#fff"/><circle cx="20" cy="18" r="2.5" fill="#222"/></svg></div>
    <h3>Lorem Ipsum Dummy</h3>
    <p>Nulla consequat massa quis enim. Veronum versus Donec pede justo, fringilla vel, aliquet nec, vulputate eget, in enim justo, rhoncus ut, imperdiet a, venenatis vitae</p>
    <span class="more">Read More</span>
  </div>
</div>

<div class="abs side-social" aria-label="Share links"><span><i></i></span><span><i></i></span></div>

<section class="abs newsletter" role="img" aria-label="Dimmed photo of a person working at a desk behind the newsletter form">
  <h2>For Latest Update Sign Up Our<br>Newsletter</h2>
  <div class="abs rule"></div>
  <p class="sub">Contrary to popular belief, Lorem Ipsum is not simply random text.</p>
  <div class="field" style="left:99px"></div>
  <div class="field" style="left:526px"></div>
  <div class="submit">SUBMIT</div>
</section>

<h2 class="abs section-title" style="top:1894px">Latest From The Blog</h2>
<div class="abs rule" style="top:1952px"></div>

<article class="abs post" style="left:99px;top:2008px">
  <div class="photo" role="img" aria-label="Photo of a woman in sunglasses outdoors" style="background:linear-gradient(135deg,#6d8a4a,#d9b48a)"></div>
  <div class="body"><h4>SWEET SAMANTHA<br>IN SUNSET ON 2015</h4><p class="meta">IN: <b>SOCIAL, MOMENTS</b><br>MARCH 9, 2015 BY <b>DARA VOSS</b></p><span class="cont">CONTINUE READING</span></div>
</article>
<article class="abs post right" style="left:601px;top:2008px">
  <div class="photo" role="img" aria-label="Photo of a man browsing a clothing rail" style="background:linear-gradient(135deg,#3c3630,#8a7a68)"></div>
  <div class="body"><h4>BRAND NEW<br>SELECTION OF FASHION</h4><p class="meta">IN: <b>SOCIAL, MOMENTS</b><br>MARCH 15, 2015 BY <b>DARA VOSS</b></p><span class="cont">CONTINUE READING</span></div>
</article>
<article class="abs post" style="left:99px;top:2224px">
  <div class="photo" role="img" aria-label="Photo of a woman walking down a tree-lined park path" style="background:linear-gradient(135deg,#4f6a3a,#b9b7a6)"></div>
  <div class="body"><h4>MY FIRST TRIP TO<br>NEW YORK</h4><p class="meta">IN: <b>SOCIAL, MOMENTS</b><br>APRIL 1, 2015 BY <b>DARA VOSS</b></p><span class="cont">CONTINUE READING</span></div>
</article>
<article class="abs post right" style="left:601px;top:2224px">
  <div class="photo" role="img" aria-label="Photo of breakfast plates on a cafe table" style="background:linear-gradient(135deg,#c9a27a,#7a4a2e)"></div>
  <div class="body"><h4>NEW BREAKFAST CAFE<br>OPENS TODAY</h4><p class="meta">IN: <b>SOCIAL, MOMENTS</b><br>MARCH 25, 2015 BY <b>DARA VOSS</b></p><span class="cont">CONTINUE READING</span></div>
</article>
<div class="abs dots" style="left:562px;top:2469px"><i></i><i></i><i class="on"></i><i></i></div>

<div class="abs clients">
  <span style="color:#d5202a">Norbeck</span>
  <span style="color:#1b61a8">Velora</span>
  <span style="color:#d5202a">Tamsin</span>
  <span style="color:#2a6db5">Quillon</span>
  <span style="color:#e8b400">Bramwell</span>
</div>

<footer class="abs footer" role="img" aria-label="Blue-tinted photo of a city skyline behind the contact area">
  <h2 class="abs section-title">GET IN TOUCH</h2>
  <div class="abs rule"></div>
  <h5 style="left:99px;top:152px">We'd Love to Hear From You, Get In Touch With Us!</h5>
  <p class="copy">We welcome questions about benchmarking, strategy reviews and technology audits for contact centres of every size. Tell us a little about your team, your current goals and the challenges you face, and one of our consultants will reply within two working days with ideas on next steps and a suggested time to talk further.</p>
  <div class="field" style="left:92px;top:275px;width:232px">Name (required)</div>
  <div class="field" style="left:348px;top:275px;width:240px">Email (required)</div>
  <div class="field" style="left:612px;top:275px;width:231px">Website</div>
  <div class="field" style="left:99px;top:315px;width:744px;height:154px">Comment ...</div>
  <h5 style="left:870px;top:152px">Contact Info</h5>
  <div class="f-rule" style="left:986px;top:162px;width:115px"></div>
  <p class="contact">Place Your Address:<br>Telephone:<br>Fax:<br>Email:</p>
  <h5 style="left:870px;top:350px">Get Social</h5>
  <div class="f-rule" style="left:968px;top:360px;width:133px"></div>
  <div class="social-grid" aria-label="Social links">
    <i></i><i></i><i></i><i></i><i></i><i></i><i></i><i></i>
    <i></i><i></i><i></i><i></i><i></i><i></i><i></i><i></i>
    <i></i><i></i>
  </div>
  <p class="legal">Copyright 2015 &nbsp;|&nbsp; All Rights Reserved &nbsp;|&nbsp; Powered by Brightmere</p>
</footer>

</body>
</html>
```